Business Card Design

We need a business card for a well established Semi Trailer Hire company. I am looking for a new start as we are moving so would like to update our Business Cards and Letter heads.
We hire Semi Trailers to Transport companies.
The colour of our Trailers are Cherry Red so this must be the prominent colour.
I do not want any pictures of trailers on the design.
I do not want the design to be flowery in anyway as we are in the transport industry.
Simple yet effective

Business

Varno Tolt Hire Pty Ltd
Ros Penbury
Director
Ph: 03 9412 5038
Mobile: 0427 836 207
ros.penbury@varnotolt-example.com.au
www.varnotolt-example.com.au
218-224 Dunmore Road, Yarraville

```html
<!DOCTYPE html>
<html lang="en">
<head>
<meta charset="utf-8">
<title>Varno Tolt Hire Pty Ltd – Business Card</title>
<link href="https://fonts.googleapis.com/css2?family=Oswald:wght@300;400;600&family=Roboto+Condensed:wght@400;700&display=swap" rel="stylesheet">
<style>
  :root {
    --backdrop: #f6c3c3;
    --cherry: #c41d24;
    --cherry-deep: #8e1117;
    --cherry-light: #e03038;
    --silver: #e9e6e6;
    --paper: #ffffff;
    --ink: #1d1d1d;
    --rule: #c9c9c9;
  }
  * { box-sizing: border-box; margin: 0; padding: 0; }
  html, body {
    width: 1200px; height: 900px; overflow: hidden;
    background: var(--backdrop);
  }
  .canvas {
    width: 1200px; height: 900px;
    display: flex; align-items: center; justify-content: center; gap: 40px;
  }
  .card {
    position: relative;
    width: 520px; height: 300px;
    border-radius: 4px;
    overflow: hidden;
    box-shadow: 0 14px 30px rgba(120, 30, 30, 0.25);
  }

  /* Front */
  .card-front {
    background: radial-gradient(circle at 58% 38%, var(--cherry-light) 0%, var(--cherry) 40%, var(--cherry-deep) 100%);
    display: flex; align-items: center; justify-content: center;
  }
  .front-lockup {
    display: flex; flex-direction: column; align-items: center;
    padding: 16px 0;
    border-top: 1px solid var(--silver);
    border-bottom: 1px solid var(--silver);
    width: 330px;
  }
  .front-name {
    font-family: "Oswald", sans-serif;
    font-weight: 300;
    font-size: 36px;
    letter-spacing: 0.3em;
    margin-right: -0.3em;
    text-transform: uppercase;
    color: var(--silver);
    line-height: 1.1;
  }
  .front-sub {
    font-family: "Oswald", sans-serif;
    font-weight: 300;
    font-size: 20px;
    letter-spacing: 0.12em;
    margin-right: -0.12em;
    text-transform: uppercase;
    color: var(--silver);
    line-height: 1.2;
  }

  /* Back */
  .card-back { background: var(--paper); }
  .back-band {
    position: absolute; left: 0; top: 0;
    width: 140px; height: 300px;
  }
  .company-block {
    position: absolute; left: 150px; top: 30px; right: 24px;
  }
  .company-block::before {
    content: ""; display: block;
    width: 120px; height: 1px; background: var(--cherry);
    margin-bottom: 6px;
  }
  .company {
    font-family: "Oswald", sans-serif;
    font-weight: 600;
    font-size: 27px;
    line-height: 1.15;
    text-transform: uppercase;
    color: var(--cherry);
    letter-spacing: 0.02em;
    white-space: nowrap;
    padding-bottom: 5px;
    border-bottom: 1px solid var(--cherry);
  }
  .address {
    margin-top: 6px;
    font-family: "Roboto Condensed", sans-serif;
    font-weight: 700; font-size: 14px;
    color: var(--ink);
    white-space: nowrap;
  }
  .person {
    position: absolute; left: 150px; top: 156px; width: 100px;
    font-family: "Roboto Condensed", sans-serif;
  }
  .person-name {
    font-family: "Oswald", sans-serif;
    font-weight: 400; font-size: 17px;
    color: var(--cherry);
    text-transform: uppercase;
    white-space: nowrap;
  }
  .person-role { font-weight: 700; font-size: 13px; color: var(--ink); }
  .divider {
    position: absolute; left: 256px; top: 150px;
    width: 1px; height: 110px; background: var(--rule);
  }
  .contacts {
    position: absolute; left: 268px; top: 150px;
    list-style: none;
    font-family: "Roboto Condensed", sans-serif;
    font-weight: 700; font-size: 11.5px;
    color: var(--ink);
  }
  .contacts li {
    display: flex; align-items: center; gap: 7px;
    height: 26px; white-space: nowrap;
  }
  .contact-icon { width: 14px; height: 14px; flex: none; }
</style>
</head>
<body>
<main class="canvas">
  <section class="card card-front" aria-label="Card front">
    <div class="front-lockup">
      <p class="front-name">Varno Tolt</p>
      <p class="front-sub">Hire Pty Ltd</p>
    </div>
  </section>

  <section class="card card-back" aria-label="Card back">
    <svg class="back-band" viewBox="0 0 140 300" aria-hidden="true">
      <path d="M0 0 H70 Q20 150 110 300 H0 Z" fill="var(--cherry)"/>
    </svg>
    <div class="company-block">
      <h1 class="company">Varno Tolt Hire Pty Ltd</h1>
      <p class="address">218-224 Dunmore Road, Yarraville</p>
    </div>

    <div class="person">
      <p class="person-name">Ros Penbury</p>
      <p class="person-role">Director</p>
    </div>
    <div class="divider"></div>

    <ul class="contacts">
      <li>
        <svg class="contact-icon" viewBox="0 0 14 14" aria-hidden="true">
          <circle cx="7" cy="7" r="7" fill="var(--cherry)"/>
          <path d="M4.3 3.6 L5.8 3.4 L6.4 5.2 L5.5 5.9 Q6.2 7.6 8 8.5 L8.7 7.6 L10.5 8.2 L10.3 9.7 Q6 10 4.3 3.6 Z" fill="#fff"/>
        </svg>03 9412 5038</li>
      <li>
        <svg class="contact-icon" viewBox="0 0 14 14" aria-hidden="true">
          <circle cx="7" cy="7" r="7" fill="var(--cherry)"/>
          <rect x="5" y="3.3" width="4" height="7.4" rx="0.8" fill="#fff"/>
          <rect x="5.8" y="4.3" width="2.4" height="4.6" fill="var(--cherry)"/>
        </svg>0427 836 207</li>
      <li>
        <svg class="contact-icon" viewBox="0 0 14 14" aria-hidden="true">
          <circle cx="7" cy="7" r="7" fill="var(--cherry)"/>
          <rect x="3.5" y="4.5" width="7" height="5" fill="#fff"/>
          <path d="M3.5 4.5 L7 7.4 L10.5 4.5" fill="none" stroke="var(--cherry)" stroke-width="0.8"/>
        </svg>ros.penbury@varnotolt-example.com.au</li>
      <li>
        <svg class="contact-icon" viewBox="0 0 14 14" aria-hidden="true">
          <circle cx="7" cy="7" r="7" fill="var(--cherry)"/>
          <circle cx="7" cy="7" r="3.6" fill="none" stroke="#fff" stroke-width="0.9"/>
          <path d="M3.4 7 H10.6 M7 3.4 V10.6" stroke="#fff" stroke-width="0.8"/>
        </svg>www.varnotolt-example.com.au</li>
    </ul>
  </section>
</main>
</body>
</html>
```